Redesign website for small print company

Vindaborgprent is a small printing company in Iceland mainly servicing Students, schools, etc. We are also doing all kind of other jobs, like business cards, book printing, brochure printing etc. We are also selling books online.
Our website is: www.vindaborgprent.is
What we are looking for is:
- Web Design (Uncoded - PSD layout only)
- Mobile friendly design, using our current color scheme: Red, green, yellow and light gray.
- Clean simple design
- Simple, light and easy to use.
- More menu Items/drop down
Industry/Entity Type
Digital Printing
Number of Pages Required
5+ page
Requirements
Must have
- Easy navigation
- Designed for mobile
- Current color scheme (see logo)
Nice to have
- Icon based products

```html
<!DOCTYPE html>
<html lang="is">
<head>
<meta charset="utf-8">
<title>Vindaborgprent</title>
<link href="https://fonts.googleapis.com/css2?family=Montserrat:wght@600;700;800&family=Mulish:wght@400;600;700&display=swap" rel="stylesheet">
<style>
:root{
  --red:#e8392c;
  --green:#0a6a34;
  --yellow:#fcd200;
  --gray:#ececec;
  --gray-light:#f2f2f2;
  --ink:#1b1b1b;
  --muted:#555;
  --white:#fff;
  --line:#e2e2e2;
}
*{box-sizing:border-box;margin:0;padding:0}
html,body{width:1200px;height:3814px;overflow:hidden}
body{font-family:"Mulish",sans-serif;color:var(--ink);background:var(--white);font-size:13px}
.wrap{width:936px;margin:0 auto;position:relative}
h1,h2,h3,.brand{font-family:"Montserrat",sans-serif}

.topbar{height:56px;background:var(--gray);display:flex;align-items:center;justify-content:center;font-size:12px;font-weight:600}
.topbar b{font-weight:800}

.site-header{height:128px;background:var(--white)}
.site-header .wrap{height:100%;display:flex;align-items:center;justify-content:space-between}
.brand{display:flex;align-items:center;gap:10px;font-weight:800;font-size:25px;letter-spacing:.5px}
.brand-mark{width:32px;height:32px;background:var(--red)}
.nav{display:flex;align-items:center;gap:28px;font-size:14px;font-weight:600}
.nav .tools{display:flex;gap:18px;margin-left:8px}

.hero{height:530px;background:var(--gray);position:relative}
.hero .wrap{padding-top:92px;height:100%}
.hero h1{font-size:45px;font-weight:800;letter-spacing:1px;line-height:1}
.hero .price{font-family:"Montserrat",sans-serif;font-size:24px;font-weight:600;margin:22px 0 24px}
.hero p{width:545px;font-size:13px;line-height:1.65;margin-bottom:22px}
.hero .actions{display:flex;align-items:center;gap:28px;margin-top:12px}
.btn{display:inline-flex;align-items:center;justify-content:center;background:var(--red);color:var(--white);font-weight:700;font-size:13px;border-radius:2px}
.btn-lg{width:195px;height:36px}
.share{display:flex;align-items:center;gap:6px;border:1px solid #ccc;background:#f8f8f8;padding:3px 10px;font-size:10px;font-weight:700}
.share i{width:10px;height:10px;background:#3b5a96;display:block}
.book-cover{position:absolute;left:676px;top:60px;width:120px;height:390px;background:linear-gradient(160deg,#fafafa 0%,#f2f2f2 45%,#e5e0d6 100%);box-shadow:8px 8px 0 #d8d4cc, 12px 14px 18px rgba(0,0,0,.15)}

.welcome{height:320px;background:var(--green);color:var(--white);text-align:center}
.welcome h2{padding-top:62px;font-size:29px;font-weight:800;letter-spacing:.5px}
.welcome p{width:640px;margin:22px auto 0;font-size:13.5px;line-height:1.6}
.signup{display:flex;justify-content:center;gap:12px;margin-top:30px}
.signup .field{width:345px;height:34px;background:var(--white);border-radius:2px;color:#999;font-size:11px;text-align:left;padding:10px 12px}
.signup .submit{width:113px;height:34px;border:1px solid var(--white);border-radius:2px;font-weight:700;font-size:14px;display:flex;align-items:center;justify-content:center}

.services{height:605px}
.services .wrap{display:flex;justify-content:space-between;padding-top:115px}
.service{width:295px;height:385px;background:var(--gray-light);padding:0 28px;position:relative}
.service.is-featured{background:var(--yellow)}
.service svg{position:absolute;left:50%;top:62px;transform:translateX(-50%)}
.service h3{position:absolute;left:28px;top:253px;font-size:16px;font-weight:700}
.service p{position:absolute;left:28px;right:28px;top:282px;font-size:11px;line-height:1.6}

.categories{height:760px;background:var(--gray)}
.categories h2{padding-top:80px;font-size:25px;font-weight:800;letter-spacing:.5px}
.cat-grid{display:grid;grid-template-columns:repeat(3,295px);justify-content:space-between;row-gap:23px;margin-top:40px}
.cat{height:250px;background:var(--white);text-align:center;padding-top:38px}
.cat svg{height:54px}
.cat h3{font-size:15px;font-weight:700;margin-top:18px}
.cat p{width:215px;margin:12px auto 0;font-size:11px;line-height:1.6;color:var(--muted)}
.cat .more{display:block;font-size:11px;font-weight:700;margin-top:12px}

.products{height:1110px}
.products h2{text-align:center;padding-top:130px;font-size:32px;font-weight:800;letter-spacing:1px}
.products .rule{width:52px;height:3px;background:var(--ink);margin:20px auto 0}
.prod-grid{display:grid;grid-template-columns:repeat(3,295px);justify-content:space-between;row-gap:38px;margin-top:66px}
.prod{height:393px;border:1px solid var(--line);text-align:center}
.prod .shot{height:205px}
.prod h3{font-size:15px;font-weight:700;margin-top:26px}
.prod .cost{color:var(--green);font-weight:700;font-size:13px;margin-top:6px}
.prod p{width:240px;margin:12px auto 0;font-size:11px;line-height:1.55;color:var(--muted)}
.btn-sm{width:96px;height:29px;font-size:11px;margin-top:14px}

.site-footer{height:304px;background:var(--gray);text-align:center}
.foot-nav{padding-top:75px;display:flex;justify-content:center;gap:12px;font-size:12px;font-weight:600}
.foot-social{margin:26px auto 0;width:14px;height:14px;background:#222}
.copy{margin-top:40px;font-size:10px}
.pay{display:flex;justify-content:center;gap:12px;margin-top:14px;font-size:10px;font-weight:700}
</style>
</head>
<body>

<div class="topbar">Sími: 555 0142 | verk@vindaborgprent.is | <b>&nbsp;Mán - Fös: 9-17</b></div>

<header class="site-header">
  <div class="wrap">
    <div class="brand"><span class="brand-mark"></span>VINDABORGPRENT</div>
    <nav class="nav">
      <span>Heim</span><span>Þjónusta</span><span>Skil á verkum</span><span>Um okkur</span>
      <span class="tools">
        <svg width="16" height="16" viewBox="0 0 16 16" fill="none" stroke="#222" stroke-width="2"><circle cx="6.5" cy="6.5" r="5"/><path d="M10.5 10.5 15 15"/></svg>
        <svg width="14" height="16" viewBox="0 0 14 16" fill="none" stroke="#222" stroke-width="2"><rect x="1" y="5" width="12" height="10"/><path d="M4 5V3a3 3 0 0 1 6 0v2"/></svg>
      </span>
    </nav>
  </div>
</header>

<section class="hero">
  <div class="wrap">
    <h1>FRJÁLST FLÆÐI</h1>
    <div class="price">4.990 kr</div>
    <p>Frjálst flæði, leiðarvísir, er handbók jafnt fyrir einstaklinga í sjálfsnámi sem og kennara sem ætla sér að stíga út í óvissu skapandi vinnu ásamt nemendum sínum.</p>
    <p>Hér er kynnt til sögunnar aðferðafræði sem auðvelt er að tileinka sér og þróa eigin leiðir útfrá. Bókin byggir á þekkingu og reynslu Sólveigar Hrafnsdóttur, myndlistarkonu, af kennslu við Listaskólann í Vindaborg og áratuga starfi á mörkum listgreina.</p>
    <div class="actions">
      <span class="btn btn-lg">Find out more</span>
      <span class="share"><i></i>DEILA</span>
    </div>
    <div class="book-cover" role="img" aria-label="Bókarkápa Frjálst flæði með litríkum slettum"></div>
  </div>
</section>

<section class="welcome">
  <h2>VELKOMIN Í VINDABORGPRENT</h2>
  <p>Vindaborgprent er fyrirtæki staðsett á háskólasvæðinu sem hefur sérhæft sig í að þjónusta skólafólk, ásamt því að sinna allri almennri prentun fyrir almenning.</p>
  <div class="signup"><div class="field">Email Address</div><div class="submit">Subscribe</div></div>
</section>

<section class="services">
  <div class="wrap">
    <div class="service">
      <svg width="130" height="110" viewBox="0 0 130 110" fill="none" stroke="var(--red)" stroke-width="7" stroke-linejoin="round"><rect x="5" y="28" width="120" height="76" rx="12"/><path d="M42 28V12a6 6 0 0 1 6-6h34a6 6 0 0 1 6 6v16"/></svg>
      <h3>SENDA VERK</h3>
      <p>Our Prep Path video series, we take complicated certification exams</p>
    </div>
    <div class="service is-featured">
      <svg width="90" height="110" viewBox="0 0 90 110" fill="none" stroke="#111" stroke-width="6" stroke-linejoin="round"><path d="M40 10C15 10 4 32 6 55c2 25 20 40 38 40 10 0 12-8 8-14s-2-12 6-12c10 0 16-8 16-22C74 25 60 10 40 10z"/><circle cx="30" cy="36" r="6"/><circle cx="24" cy="60" r="6"/><circle cx="50" cy="30" r="5"/><path d="M80 15l-6 50"/><path d="M70 70l8 2-2 14-8-2z"/></svg>
      <h3>HANNA VERK</h3>
      <p>Our Prep Path book series will get you certified in the shortest amount of time.</p>
    </div>
    <div class="service">
      <svg width="80" height="120" viewBox="0 0 80 120" fill="none" stroke="var(--green)" stroke-width="7" stroke-linecap="round"><path d="M8 30a32 26 0 1 1 40 24c-8 4-10 10-10 22"/><circle cx="38" cy="104" r="5" fill="var(--green)"/></svg>
      <h3>FA TILBOD</h3>
      <p>Our quiz apps prepare you for the certification exam while on the go!</p>
    </div>
  </div>
</section>

<section class="categories">
  <div class="wrap">
    <h2>VÖRUFLOKKAR</h2>
    <div class="cat-grid">
      <div class="cat">
        <svg width="40" height="54" viewBox="0 0 40 52" fill="none" stroke="var(--red)" stroke-width="2.5"><path d="M8 4h26v40a4 4 0 0 1-4 4H6a4 4 0 0 1-4-4v-4h24v4"/><path d="M8 4a4 4 0 0 0-4 4v4h4"/><path d="M14 14h14M14 21h14M14 28h14"/></svg>
        <h3>RITGERÐIR</h3><p>Using our Prep Path video series, we take complicated certification exams</p><span class="more">Read more</span>
      </div>
      <div class="cat">
        <svg width="56" height="54" viewBox="0 0 56 46" fill="none" stroke="var(--green)" stroke-width="2.5"><rect x="12" y="4" width="40" height="26" rx="2"/><rect x="3" y="14" width="40" height="27" rx="2" fill="#fff"/><circle cx="14" cy="26" r="4"/><path d="M22 22h14M22 28h14M10 35h26"/></svg>
        <h3>NAFNSPJÖLD</h3><p>Using our Prep Path video series, we take complicated certification exams</p><span class="more">Read more</span>
      </div>
      <div class="cat">
        <svg width="56" height="54" viewBox="0 0 56 46" fill="none" stroke="var(--yellow)" stroke-width="2.5"><path d="M28 8C20 3 10 3 3 6v34c7-3 17-3 25 2 8-5 18-5 25-2V6C46 3 36 3 28 8zM28 8v34"/><path d="M9 14h13M9 21h13M34 14h13M34 21h13"/></svg>
        <h3>BÆKLINGAR</h3><p>Using our Prep Path video series, we take complicated certification exams</p><span class="more">Read more</span>
      </div>
      <div class="cat">
        <svg width="40" height="54" viewBox="0 0 40 54" fill="none" stroke="var(--green)" stroke-width="2.5"><path d="M20 2v6"/><rect x="6" y="8" width="28" height="22"/><path d="M6 36h28M10 30l-6 22M30 30l6 22M20 36v16"/></svg>
        <h3>RITGERÐIR</h3><p>Using our Prep Path video series, we take complicated certification exams</p><span class="more">Read more</span>
      </div>
      <div class="cat">
        <svg width="40" height="54" viewBox="0 0 40 54" fill="none" stroke="var(--red)" stroke-width="2.5"><rect x="4" y="8" width="32" height="42" rx="2"/><path d="M12 8V3M28 8V3"/><rect x="10" y="16" width="20" height="16"/><path d="M10 38h20M10 44h14"/></svg>
        <h3>VEGGSPJÖLD</h3><p>Using our Prep Path video series, we take complicated certification exams</p><span class="more">Read more</span>
      </div>
      <div class="cat">
        <svg width="52" height="54" viewBox="0 0 52 50" fill="none" stroke="var(--green)" stroke-width="2.5"><rect x="3" y="6" width="11" height="40"/><rect x="16" y="2" width="11" height="44"/><rect x="30" y="8" width="9" height="38"/><path d="M42 10l7 2-8 34-7-2"/><path d="M3 14h11M3 38h11M16 10h11M16 38h11"/></svg>
        <h3>KENNSLUBÆKUR</h3><p>Using our Prep Path video series, we take complicated certification exams</p><span class="more">Read more</span>
      </div>
    </div>
  </div>
</section>

<section class="products">
  <div class="wrap">
    <h2>VÖRUR</h2>
    <div class="rule"></div>
    <div class="prod-grid">
      <div class="prod">
        <div class="shot" role="img" aria-label="Brotnir bæklingar í A3 á borði" style="background:linear-gradient(135deg,#e9e7e3,#b7aea4 60%,#5a6f86)"></div>
        <h3>A3 Brotnir Bæklingar</h3><div class="cost">1.000 kr</div>
        <p>Þessi tegund bæklinga er oftast prentuð á hálfglansandi 170 gr. pappír, eða 150 gr.</p>
        <span class="btn btn-sm">Shop Now</span>
      </div>
      <div class="prod">
        <div class="shot" role="img" aria-label="Prentaðar kiljur með litríkum kápum" style="background:linear-gradient(135deg,#d9d9d9,#c9407a 45%,#e7c33a 75%,#5a8f4f)"></div>
        <h3>Bókaprentun, kiljur</h3><div class="cost">$9 / month</div>
        <p>With our $9/month plan, you get unlimited access to all of our courses!</p>
        <span class="btn btn-sm">Shop Now</span>
      </div>
      <div class="prod">
        <div class="shot" role="img" aria-label="Kennslubók með bleikri kápu" style="background:linear-gradient(135deg,#f1f1f1,#e6e6e6 50%,#e02a78)"></div>
        <h3>Kennslubækur</h3><div class="cost">$9 / month</div>
        <p>With our $9/month plan, you get unlimited access to all of our courses!</p>
        <span class="btn btn-sm">Shop Now</span>
      </div>
      <div class="prod">
        <div class="shot" role="img" aria-label="Ferðamannabæklingar í stafla" style="background:linear-gradient(135deg,#2b2b2b,#8a3a2a 45%,#9fb1c2)"></div>
        <h3>Túristabæklingur</h3><div class="cost">1.000 kr</div>
        <p>Þessi tegund bæklinga er oftast prentuð á hálfglansandi 170 gr. pappír, eða 150 gr.</p>
        <span class="btn btn-sm">Shop Now</span>
      </div>
      <div class="prod">
        <div class="shot" role="img" aria-label="Tvö hvít kort með rauðum myndum" style="background:linear-gradient(135deg,#bcd6ec,#f3f3f3 45%,#d94a4a)"></div>
        <h3>Bókaprentun, kiljur</h3><div class="cost">$9 / month</div>
        <p>With our $9/month plan, you get unlimited access to all of our courses!</p>
        <span class="btn btn-sm">Shop Now</span>
      </div>
      <div class="prod">
        <div class="shot" role="img" aria-label="Upprúlluð svört veggspjöld" style="background:linear-gradient(135deg,#f2f2f2,#1e1e1e 55%,#e9e9e9)"></div>
        <h3>Veggspjald A0</h3><div class="cost">$9 / month</div>
        <p>With our $9/month plan, you get unlimited access to all of our courses!</p>
        <span class="btn btn-sm">Shop Now</span>
      </div>
    </div>
  </div>
</section>

<footer class="site-footer">
  <div class="foot-nav"><span>Heim</span><span>Þjónusta</span><span>Skil á verkum</span><span>Um okkur</span></div>
  <div class="foot-social"></div>
  <div class="copy">© 2018, Vindaborgprent / Store Designed by Norðvik</div>
  <div class="pay"><span>Payla</span><span>Kortex</span></div>
</footer>

</body>
</html>
```